Ferris Contracting LLC Business Card Design

I am looking for a creative and unique business card design. We are a commercial construction general contractor. With the name "FERRIS" Contracting, I am hoping to see some neat designs that correlate with the name.

```html
<!DOCTYPE html>
<html lang="en">
<head>
<meta charset="utf-8">
<title>Ferris Contracting LLC – Business Card</title>
<link href="https://fonts.googleapis.com/css2?family=Cormorant+Garamond:wght@500&family=Montserrat:wght@400;800&display=swap" rel="stylesheet">
<style>
  :root {
    --page-bg: #fafafa;
    --card-bg: #ffffff;
    --brand-blue: #1b87cf;
    --text-grey: #4a4d52;
    --rule-grey: #b9bcc0;
  }
  * { box-sizing: border-box; margin: 0; padding: 0; }
  html, body {
    width: 1200px; height: 800px; overflow: hidden;
    background: var(--page-bg);
  }
  .canvas { position: relative; width: 1200px; height: 800px; }
  .card {
    position: absolute; top: 241px;
    width: 514px; height: 286px;
    background: var(--card-bg);
    border: 1px solid #ececec;
  }
  .card--front { left: 62px; }
  .card--back { left: 623px; }

  .brand {
    position: absolute; inset: 0;
    display: flex; align-items: center; justify-content: center; gap: 18px;
    color: var(--brand-blue);
    font-family: "Montserrat", sans-serif; font-weight: 800;
  }
  .brand__dot {
    width: 62px; height: 62px; border-radius: 50%;
    background: var(--brand-blue);
  }
  .brand__name { display: flex; flex-direction: column; line-height: 1; }
  .brand__word { font-size: 72px; letter-spacing: 1px; }
  .brand__tag { font-size: 19px; letter-spacing: 11px; margin-top: 8px; }

  .holder {
    position: absolute; left: 34px; top: 27px;
    font-family: "Cormorant Garamond", serif; font-weight: 500;
    font-size: 20px; letter-spacing: 2.4px; color: var(--text-grey);
  }
  .rule {
    position: absolute; left: 34px; height: 1px;
  }
  .rule--top {
    top: 70px; width: 430px;
    background: linear-gradient(90deg, var(--brand-blue), rgba(27,135,207,0.1));
  }
  .rule--bottom {
    top: 263px; width: 460px;
    background: linear-gradient(90deg, var(--rule-grey), rgba(185,188,192,0.15));
  }
  .contact-list { list-style: none; }
  .contact {
    position: absolute; left: 34px;
    display: flex; align-items: center; gap: 15px;
    font-family: "Montserrat", sans-serif; font-size: 15.5px;
    color: var(--text-grey);
  }
  .contact svg { width: 20px; height: 20px; fill: var(--brand-blue); flex: none; }
  .contact--phone { top: 93px; }
  .contact--email { top: 130px; }
  .contact--web { top: 169px; }
  .contact--address { top: 206px; }
</style>
</head>
<body>
<main class="canvas">
  <section class="card card--front" aria-label="Card front">
    <div class="brand">
      <span class="brand__dot" aria-hidden="true"></span>
      <div class="brand__name">
        <span class="brand__word">FERRIS</span>
        <span class="brand__tag">CONTRACTING</span>
      </div>
    </div>
  </section>

  <section class="card card--back" aria-label="Card back">
    <h1 class="holder">DANIEL MERCER</h1>
    <div class="rule rule--top"></div>
    <ul class="contact-list">
      <li class="contact contact--phone">
        <svg viewBox="0 0 24 24" aria-hidden="true"><path d="M6.6 10.8a15.1 15.1 0 0 0 6.6 6.6l2.2-2.2c.3-.3.7-.4 1-.2 1.1.4 2.3.6 3.6.6.6 0 1 .4 1 1V20c0 .6-.4 1-1 1A17 17 0 0 1 3 4c0-.6.4-1 1-1h3.5c.6 0 1 .4 1 1 0 1.3.2 2.5.6 3.6.1.3 0 .7-.2 1z"/></svg>
        <span>+1 (555) 214-7390</span>
      </li>
      <li class="contact contact--email">
        <svg viewBox="0 0 24 24" aria-hidden="true"><path d="M2 5h20v14H2z M3.5 6.5 12 12.5l8.5-6" fill="var(--brand-blue)"/><path d="M3 6l9 6.5L21 6" fill="none" stroke="#fff" stroke-width="1.6"/></svg>
        <span>daniel@ferriscontracting.com</span>
      </li>
      <li class="contact contact--web">
        <svg viewBox="0 0 24 24" aria-hidden="true"><g fill="none" stroke="var(--brand-blue)" stroke-width="1.6"><circle cx="12" cy="12" r="9"/><ellipse cx="12" cy="12" rx="4" ry="9"/><path d="M3 12h18M4.5 7.5h15M4.5 16.5h15"/></g></svg>
        <span>www.ferriscontracting.com</span>
      </li>
      <li class="contact contact--address">
        <svg viewBox="0 0 24 24" aria-hidden="true"><path d="M12 2a7 7 0 0 0-7 7c0 5 7 13 7 13s7-8 7-13a7 7 0 0 0-7-7zm0 9.5A2.5 2.5 0 1 1 12 6.5a2.5 2.5 0 0 1 0 5z"/></svg>
        <span>418 Harbor Lane, Millbrook, USA 20917</span>
      </li>
    </ul>
    <div class="rule rule--bottom"></div>
  </section>
</main>
</body>
</html>
```